makeup banner

Need a pull up banner design for a freelance makeup artist with minimal information and one picture.
details are:
Glambyroselyn
info@glambyroselyn-studio.net
0437862139
specialising in bridal, photography and special event makeup
instagram - glamby_roselyn
facebook - Glambyroselyn

Industry/Entity Type

Makeup

```html
<!DOCTYPE html>
<html lang="en">
<head>
<meta charset="utf-8">
<title>Glam by Roselyn – Pull Up Banner</title>
<link href="https://fonts.googleapis.com/css2?family=Great+Vibes&family=Satisfy&family=Questrial&display=swap" rel="stylesheet">
<style>
  :root {
    --ink: #111111;
    --paper: #ffffff;
    --sky: #f4f6f3;
    --meadow: #9aa94a;
    --sun: #f3d79a;
    --warm: #c98a52;
    --phone-green: #5fd43a;
    --mail-blue: #3fb4f0;
    --social-square: #2a2a2a;
  }
  * { margin: 0; padding: 0; box-sizing: border-box; }
  html, body { width: 1200px; height: 2842px; overflow: hidden; background: var(--paper); }
  .banner { position: relative; width: 1200px; height: 2842px; background: var(--paper); color: var(--ink); }

  .hero-photo {
    position: absolute; left: 0; top: 0; width: 1200px; height: 1595px;
    background:
      radial-gradient(ellipse 520px 700px at 850px 900px, rgba(222,160,120,0.85), rgba(222,160,120,0) 70%),
      radial-gradient(ellipse 700px 500px at 250px 700px, rgba(243,215,154,0.9), rgba(243,215,154,0) 75%),
      linear-gradient(180deg, var(--sky) 0%, #e9ecd8 14%, #b9c27a 40%, var(--meadow) 65%, #8c8a3a 100%);
  }
  .header-wash {
    position: absolute; left: 0; top: 0; width: 1200px; height: 420px;
    background: linear-gradient(180deg, rgba(255,255,255,0.85) 0%, rgba(255,255,255,0.5) 60%, rgba(255,255,255,0) 100%);
  }
  .brand-name {
    position: absolute; left: 50px; top: 60px;
    font-family: "Great Vibes", cursive; font-weight: 400;
    font-size: 190px; line-height: 1; color: var(--ink);
  }

  .specialty-intro {
    position: absolute; left: 0; top: 1615px; width: 1200px; text-align: center;
    font-family: "Satisfy", cursive; font-size: 86px; line-height: 1.2;
  }
  .specialty-list {
    position: absolute; left: 0; top: 1800px; width: 1200px; text-align: center;
    font-family: "Questrial", sans-serif; text-transform: uppercase;
    font-size: 56px; letter-spacing: 8px; line-height: 92px;
  }

  .contact-list { position: absolute; left: 50px; top: 2062px; list-style: none; }
  .contact-item { display: flex; align-items: center; height: 126px; margin-bottom: 66px; }
  .contact-icon { width: 126px; height: 126px; flex: none; }
  .contact-label {
    margin-left: 70px;
    font-family: "Questrial", sans-serif; font-size: 38px; letter-spacing: 5px;
    text-transform: uppercase; color: var(--ink);
  }
  .social-square { width: 126px; height: 126px; flex: none; background: var(--social-square); border-radius: 8px; }
</style>
</head>
<body>
<main class="banner">
  <div class="hero-photo" role="img" aria-label="Sunlit portrait of a smiling woman with long hair and a jewelled hair vine in a grassy meadow"></div>
  <div class="header-wash"></div>
  <h1 class="brand-name">Glam by Roselyn</h1>

  <p class="specialty-intro">Specialist in:</p>
  <p class="specialty-list">Bridal, Photography &amp;<br>Special Event Makeup</p>

  <ul class="contact-list">
    <li class="contact-item">
      <svg class="contact-icon" viewBox="0 0 126 126" aria-hidden="true">
        <rect width="126" height="126" rx="28" fill="var(--phone-green)"/>
        <path d="M40 30c6-3 10 0 13 8l4 10c2 5 0 8-4 11l-3 2c4 9 11 17 20 21l3-3c3-4 6-5 11-3l10 4c8 3 10 8 7 13-4 8-11 11-20 9-25-6-44-26-50-51-2-9 2-17 9-21z" fill="#ffffff"/>
      </svg>
      <span class="contact-label">0437862139</span>
    </li>
    <li class="contact-item">
      <svg class="contact-icon" viewBox="0 0 126 126" aria-hidden="true">
        <rect width="126" height="126" rx="28" fill="var(--mail-blue)"/>
        <rect x="24" y="38" width="78" height="52" rx="4" fill="#ffffff"/>
        <path d="M26 40l37 30 37-30" fill="none" stroke="var(--mail-blue)" stroke-width="4"/>
      </svg>
      <span class="contact-label" style="text-transform:none;">info@glambyroselyn-studio.net</span>
    </li>
    <li class="contact-item">
      <span class="social-square" aria-hidden="true"></span>
      <span class="contact-label" style="text-transform:none;">Glambyroselyn</span>
    </li>
    <li class="contact-item">
      <span class="social-square" aria-hidden="true"></span>
      <span class="contact-label" style="text-transform:none;">glamby_roselyn</span>
    </li>
  </ul>
</main>
</body>
</html>
```